San Francisco corporate relocation liason

I can't seem to find what i have pictured in my head for this project. I am trying to have designed a business card that has either the San Francisco skyline or Golden Gate Bridge Silhouettein gold foil up the around half of the card and below in black letters my personal info that I need to include on card like phone number email etc.

Target Market(s)

Corporate clients I serve

Industry/Entity Type

Business

Contact Information for Business Card

Greta Holm
Corporate Relocation Expert
555.203.9186
Movewise.dtr@postlark.com

Requirements
Must have
• I would like the San francisco city skyline or Golden Gate Bridge outline in mettalic gold from the top to the middle of card and below I would like black lettering for contact information. I have included a pic of some inspiration but what I would prefer a more elegant interpretation of the image I included if possible. I had I visioned something with metallic gold and black and white or just black and white...look forward to seeing designs
Nice to have
• If possible something to signify relocation would be a plus but not necessary
• I also included below a few of examples of styles that I am drawn to if they had some element of San Francisco or relocation services

```html
<!DOCTYPE html>
<html lang="en">
<head>
<meta charset="utf-8">
<title>Greta Holm — Corporate Relocation Expert</title>
<link href="https://fonts.googleapis.com/css2?family=Montserrat:wght@700&family=Open+Sans:wght@400&display=swap" rel="stylesheet">
<style>
  :root {
    --page: #ece9e4;
    --ink: #111111;
    --paper: #ffffff;
    --gold-light: #f7e3ae;
    --gold-mid: #e2c47f;
    --gold-deep: #c9a560;
    --silhouette-top: #b99a5c;
    --silhouette: #161410;
  }
  * { margin: 0; padding: 0; box-sizing: border-box; }
  html, body {
    width: 1200px;
    height: 1000px;
    overflow: hidden;
    background: var(--page);
  }
  .sheet {
    width: 1200px;
    height: 1000px;
    display: flex;
    flex-direction: column;
    align-items: center;
    justify-content: center;
    gap: 60px;
  }
  .card {
    width: 680px;
    height: 400px;
    position: relative;
    overflow: hidden;
    box-shadow: 0 6px 18px rgba(0, 0, 0, 0.18);
  }
  .card--back {
    background: repeating-linear-gradient(
      to bottom,
      var(--ink) 0 57px,
      var(--paper) 57px 114px
    );
  }
  .card--front {
    background: linear-gradient(160deg, var(--gold-light) 0%, var(--gold-mid) 55%, var(--gold-deep) 100%);
    display: flex;
    flex-direction: column;
    align-items: center;
  }
  .skyline {
    display: block;
    width: 100%;
    height: 222px;
    flex: none;
  }
  .details {
    display: flex;
    flex-direction: column;
    align-items: center;
    margin-top: 14px;
    color: var(--ink);
  }
  .details__name {
    font-family: "Montserrat", sans-serif;
    font-weight: 700;
    font-size: 40px;
    letter-spacing: 0.5px;
    line-height: 1;
    padding-bottom: 5px;
    border-bottom: 4px solid var(--ink);
  }
  .details__title {
    font-family: "Open Sans", sans-serif;
    font-size: 23px;
    line-height: 1.25;
    margin-top: 2px;
  }
  .details__phone,
  .details__email {
    font-family: "Open Sans", sans-serif;
    font-size: 22.5px;
    line-height: 1.22;
  }
  .details__phone { margin-top: 12px; }
</style>
</head>
<body>
  <main class="sheet">
    <section class="card card--back" aria-label="Card back, black and white horizontal stripes"></section>

    <section class="card card--front">
      <svg class="skyline" viewBox="0 0 680 222" role="img" aria-label="Illustration placeholder: black silhouette of the San Francisco skyline with the Golden Gate Bridge on gold">
        <defs>
          <linearGradient id="skylineTone" x1="0" y1="0" x2="0" y2="1">
            <stop offset="0" stop-color="var(--silhouette-top)"/>
            <stop offset="1" stop-color="var(--silhouette)"/>
          </linearGradient>
        </defs>
        <rect class="skyline__area" x="0" y="26" width="680" height="170" fill="url(#skylineTone)"/>
        <rect class="skyline__ground" x="0" y="196" width="680" height="26" fill="var(--silhouette)"/>
      </svg>

      <div class="details">
        <h1 class="details__name">GRETA HOLM</h1>
        <p class="details__title">Corporate Relocation Expert</p>
        <p class="details__phone">555.203.9186</p>
        <p class="details__email">Movewise.dtr@postlark.com</p>
      </div>
    </section>
  </main>
</body>
</html>
```